Business Card & Email Signature Design || Upmarket + Luxury

Riverlume Honey, a New Zealand Manuka Honey company needs a Business Card & Email Signature design.

Our logo's are attached in Gold & Black versions, feel free to be creative with how you use the logo and it's patterns in your design.

Style:
- Looking for an Elegant, Luxurious, Upmarket feel.
- Black/Matte Black Card, Gold Foil, UV Embossing

Information to Add:

- Logo
- Company Name: Riverlume Honey
- Name: Mattias Brovell
- Title: Creative Director
- Phone: +64 2919 58 617
- Email: mattias@riverlumehoney.example
- Website: www.riverlumehoney.example

- Socials: ***For email Signature Only***
- Facebook: https://www.facebook.com/riverlumehoney/
- Instagram: https://www.instagram.com/riverlumehoney/

Target Market(s)

Asia/Europe Luxury, Upmarket

Contact Information for Business Card

- Logo
- Name: Mattias Brovell
- Phone: +64 2919 58 617

Font styles to use
Other font styles liked:
• Champagne & Limousines (Attached)

Requirements
Must have
• Business Card & Email Signature Design.

Looking for a Sleek, Luxury, Upmarket Design.

```html
<!DOCTYPE html>
<html lang="en">
<head>
<meta charset="utf-8">
<title>Riverlume Honey — Business Card</title>
<link rel="stylesheet" href="https://fonts.googleapis.com/css2?family=Josefin+Sans:wght@300;400&family=Oswald:wght@600&family=Raleway:wght@400&display=swap">
<style>
  :root {
    --bg: #2b2b2d;
    --card-black: #141414;
    --card-white: #f7f7f7;
    --gold: #c9a441;
    --ink: #2e2e2e;
    --grey: #6b6b6b;
    --green: #6aa61c;
    --purple: #4b1a82;
    --blue: #163a8a;
    --yellow: #f0c21a;
  }
  * { margin: 0; padding: 0; box-sizing: border-box; }
  html, body { width: 1200px; height: 960px; overflow: hidden; background: var(--bg); }
  .canvas {
    position: relative; width: 1200px; height: 960px;
    display: flex; flex-direction: column; align-items: center; justify-content: center; gap: 56px;
  }
  .card {
    position: relative; width: 640px; height: 366px; border-radius: 4px; overflow: hidden;
    box-shadow: 0 10px 30px rgba(0,0,0,0.35);
  }
  .card--front { background: var(--card-black); }
  .card--back { background: var(--card-white); }

  .emboss-pattern {
    position: absolute; inset: 0;
    background: radial-gradient(ellipse at 55% 45%, #222 0%, #181818 55%, var(--card-black) 100%);
  }

  .brand {
    position: absolute; display: flex; align-items: center; gap: 14px;
    font-family: "Josefin Sans", sans-serif; font-weight: 300;
    text-transform: uppercase; letter-spacing: 0.22em; white-space: nowrap;
  }
  .brand__dot { border-radius: 50%; flex: none; }
  .card--front .brand { left: 50%; top: 50%; transform: translate(-50%, -50%); color: var(--gold); font-size: 34px; }
  .card--front .brand__dot { width: 22px; height: 22px; background: var(--gold); }
  .card--back .brand { right: 48px; top: 96px; color: var(--ink); font-size: 20px; }
  .card--back .brand__dot { width: 14px; height: 14px; background: var(--ink); }

  .contact { position: absolute; left: 44px; top: 170px; }
  .contact__name {
    font-family: "Oswald", sans-serif; font-weight: 600; font-size: 26px;
    color: var(--green); text-transform: uppercase; letter-spacing: 0.01em; line-height: 1;
  }
  .contact__title { font-family: "Raleway", sans-serif; font-size: 15px; color: var(--grey); margin-top: 4px; }
  .contact__details { font-family: "Raleway", sans-serif; font-size: 14px; color: var(--grey); line-height: 1.5; margin-top: 26px; }

  .spectrum-rule { position: absolute; left: 44px; top: 242px; width: 552px; height: 2px; display: flex; }
  .spectrum-rule span { flex: 1; }
  .spectrum-rule .s1 { background: var(--purple); }
  .spectrum-rule .s2 { background: var(--blue); }
  .spectrum-rule .s3 { background: var(--green); }
  .spectrum-rule .s4 { background: var(--yellow); }

  .website {
    position: absolute; right: 44px; bottom: 40px;
    font-family: "Raleway", sans-serif; font-size: 15px; color: var(--green);
  }
</style>
</head>
<body>
<main class="canvas">
  <section class="card card--front" aria-label="Card front">
    <div class="emboss-pattern" role="img" aria-label="Faint spot-UV embossed swirl pattern on matte black"></div>
    <div class="brand"><span class="brand__dot"></span>Riverlume Honey</div>
  </section>

  <section class="card card--back" aria-label="Card back">
    <div class="brand"><span class="brand__dot"></span>Riverlume Honey</div>
    <div class="contact">
      <h1 class="contact__name">Mattias Brovell</h1>
      <p class="contact__title">Creative Director</p>
      <p class="contact__details">P. +64 2919 58 617<br>mattias@riverlumehoney.example</p>
    </div>
    <div class="spectrum-rule"><span class="s1"></span><span class="s2"></span><span class="s3"></span><span class="s4"></span></div>
    <p class="website">www.riverlumehoney.example</p>
  </section>
</main>
</body>
</html>
```